Tuition Company Flyer Design

Hi I need a flyer designed for my tutoring company. We current focus on Maths and Science mainly and on an online model of teaching. The company is called Copperfern Education. I have attached our logo. We have mainly light blue and white as our colours. I'm looking for attractive, young and cool flyers, with a high/secondary school focus. Contact information must be clearly visible. Images mandatory.

Target Market(s)

Schools and Colleges

Industry/Entity Type

Education

Requirements
Must have
• Images, Slogans, contact section
Nice to have
• Good graphics, have a clean innovative theme

```html
<!DOCTYPE html>
<html lang="en">
<head>
<meta charset="utf-8">
<title>Copperfern Education Flyer</title>
<link href="https://fonts.googleapis.com/css2?family=Oswald:wght@500;700&family=Open+Sans:ital,wght@0,400;0,600;1,600&display=swap" rel="stylesheet">
<style>
  :root{
    --blue:#2a8fe0;
    --blue-deep:#1670c4;
    --blue-light:#5fb4f2;
    --charcoal:#3b3b3d;
    --charcoal-dark:#232325;
    --grey:#d9dbdd;
    --text:#333;
    --white:#fff;
  }
  *{margin:0;padding:0;box-sizing:border-box}
  html,body{width:900px;height:1200px;overflow:hidden;background:var(--white)}
  .flyer{position:relative;width:900px;height:1200px;overflow:hidden;background:var(--white);font-family:"Open Sans",Arial,sans-serif;color:var(--text)}
  .hero-art{position:absolute;left:0;top:0}
  .brand{position:absolute;right:48px;top:38px;text-align:center;color:var(--blue);font-family:"Oswald",Arial,sans-serif;font-weight:500;font-size:44px;line-height:1}
  .brand small{display:block;font-size:20px;letter-spacing:1px;margin-top:4px}
  .slogan{position:absolute;left:610px;top:312px;width:270px;text-align:center;color:var(--white);font-family:"Oswald",Arial,sans-serif;font-weight:500;text-transform:uppercase;line-height:1.08}
  .slogan .big{font-size:46px;display:block}
  .slogan .small{font-size:30px;display:block}
  .headline{position:absolute;left:60px;top:545px;font-family:"Oswald",Arial,sans-serif;font-weight:700;font-size:56px;color:var(--blue);text-transform:uppercase;letter-spacing:.5px;line-height:1.2}
  .intro{position:absolute;left:60px;top:625px;width:790px;font-size:18px;line-height:1.4}
  .services{position:absolute;left:40px;top:742px;width:560px;height:220px;background:linear-gradient(180deg,var(--blue-light),var(--blue-deep));border-radius:0 30px 30px 0;padding:22px 0 0 46px;list-style:none}
  .services li{display:flex;align-items:center;gap:14px;color:var(--white);font-style:italic;font-weight:600;font-size:30px;line-height:46px}
  .services svg{flex:none}
  .student-photo{position:absolute;left:600px;top:718px;width:300px;height:318px;background:radial-gradient(circle at 50% 40%,#f4ddc8,#e9c7a9 35%,#e06a4f 70%,#7a5a3a)}
  .contact{position:absolute;left:60px;top:1000px;display:flex;align-items:center;gap:16px;font-family:"Oswald",Arial,sans-serif;font-weight:500;font-size:40px;color:var(--charcoal)}
  .contact .icon{width:50px;height:50px;border-radius:50%;background:var(--blue);display:flex;align-items:center;justify-content:center}
  .footer-bar{position:absolute;left:0;top:1100px;width:900px;height:72px;background:linear-gradient(180deg,var(--charcoal),var(--charcoal-dark));border-top:6px solid var(--blue);display:flex;align-items:center;padding-left:60px;color:var(--white);font-style:italic;font-weight:600;font-size:28px}
</style>
</head>
<body>
<div class="flyer">
  <svg class="hero-art" width="900" height="600" viewBox="0 0 900 600">
    <defs>
      <linearGradient id="classroom" x1="0" y1="0" x2="1" y2="1">
        <stop offset="0" stop-color="#dfe6ec"/>
        <stop offset=".45" stop-color="#e9b9a0"/>
        <stop offset="1" stop-color="#8fa7c4"/>
      </linearGradient>
      <linearGradient id="circleBlue" x1="0" y1="0" x2="0" y2="1">
        <stop offset="0" stop-color="#48a8ef"/>
        <stop offset="1" stop-color="#1670c4"/>
      </linearGradient>
    </defs>
    <path role="img" aria-label="Photo of smiling school children at desks in a classroom" d="M0,40 H520 Q600,40 640,110 Q680,180 900,180 V470 H0 Z" fill="url(#classroom)"/>
    <path d="M0,470 Q420,360 900,300 V350 Q460,400 0,520 Z" fill="var(--grey)"/>
    <path d="M0,490 Q420,390 900,330 V370 Q460,430 0,540 Z" fill="var(--charcoal)"/>
    <circle cx="745" cy="370" r="165" fill="var(--charcoal)"/>
    <circle cx="745" cy="370" r="147" fill="url(#circleBlue)" stroke="var(--white)" stroke-width="10"/>
  </svg>
  <div class="brand">Copperfern<small>Education</small></div>
  <div class="slogan">
    <span class="big">Enhancing</span>
    <span class="small">Education with</span>
    <span class="small">Modern Approach</span>
  </div>

  <h1 class="headline">Lorem ipsum dolor sit amet</h1>
  <p class="intro">Lorem ipsum dolor sit amet, consectetur adipiscing elit. Sed eu lectus tincidunt, male suada odio at, ultricies justo. Integer consequat, purus ut tristique posuere, arcu orci tincidunt orci, eget pharetra orci elit eget tortor.</p>

  <ul class="services">
    <li><svg width="26" height="26" viewBox="0 0 26 26"><circle cx="13" cy="13" r="11" fill="none" stroke="#fff" stroke-width="2.5"/><path d="M8 13.5l3.5 3.5 7-8" fill="none" stroke="#fff" stroke-width="2.5"/></svg>Maths &amp; Science coachings</li>
    <li><svg width="26" height="26" viewBox="0 0 26 26"><circle cx="13" cy="13" r="11" fill="none" stroke="#fff" stroke-width="2.5"/><path d="M8 13.5l3.5 3.5 7-8" fill="none" stroke="#fff" stroke-width="2.5"/></svg>Online teaching model</li>
    <li><svg width="26" height="26" viewBox="0 0 26 26"><circle cx="13" cy="13" r="11" fill="none" stroke="#fff" stroke-width="2.5"/><path d="M8 13.5l3.5 3.5 7-8" fill="none" stroke="#fff" stroke-width="2.5"/></svg>Interesting assignments</li>
    <li><svg width="26" height="26" viewBox="0 0 26 26"><circle cx="13" cy="13" r="11" fill="none" stroke="#fff" stroke-width="2.5"/><path d="M8 13.5l3.5 3.5 7-8" fill="none" stroke="#fff" stroke-width="2.5"/></svg>Modernised test methods</li>
  </ul>

  <div class="student-photo" role="img" aria-label="Photo of a young girl in glasses reading a book"></div>

  <div class="contact">
    <span class="icon"><svg width="26" height="26" viewBox="0 0 24 24"><path d="M6.6 10.8a15.1 15.1 0 0 0 6.6 6.6l2.2-2.2a1 1 0 0 1 1-.25 11.4 11.4 0 0 0 3.6.57 1 1 0 0 1 1 1V20a1 1 0 0 1-1 1A17 17 0 0 1 3 4a1 1 0 0 1 1-1h3.5a1 1 0 0 1 1 1c0 1.250.2 2.45.57 3.57a1 1 0 0 1-.25 1z" fill="#fff"/></svg></span>
    CONTACT US AT - 555.204.318
  </div>

  <div class="footer-bar">Our website - www.copperfern-edu.com</div>
</div>
</body>
</html>
```